Looking for a cool & simple business-card-design for digital agency

Hi!

We are a web agency that offers Reputation Management, Zorvik & Seo Services and software development. We like cool things, we like innovative styles.

We have uploaded our logo.

Project Deadline Extended Reason: Client does not want any designs with the colorful logo. Please send us submissions ONLY with the blac and white logo. What the client would like to see:1) Back of the card: is a silver logo on a black background2) front of the card with all the data, please use white background and black logo thank you Added Friday, May 8, 2015

Software

```html
<!DOCTYPE html>
<html lang="de">
<head>
<meta charset="utf-8">
<title>Velqora AG – Visitenkarte</title>
<link rel="stylesheet" href="https://fonts.googleapis.com/css2?family=Ubuntu:wght@300;400;500&display=swap">
<style>
  :root {
    --backdrop: #d8d8d9;
    --card-black: #141414;
    --card-white: #f4f4f4;
    --pattern-light: #f7f7f7;
    --pattern-mid: #dedede;
    --ink: #2b2b2b;
    --silver: #e6e6e6;
    --accent: #5cbdb2;
  }
  * { box-sizing: border-box; margin: 0; padding: 0; }
  html, body {
    width: 1200px; height: 1000px; overflow: hidden;
    background: var(--backdrop);
    font-family: "Ubuntu", sans-serif;
  }
  .canvas { position: relative; width: 1200px; height: 1000px; }
  .card {
    position: absolute; width: 500px; height: 290px;
    box-shadow: 0 3px 10px rgba(0,0,0,.18);
  }
  .card--back {
    left: 130px; top: 160px; background: var(--card-black);
    display: flex; align-items: center; justify-content: center;
  }
  .back-brand {
    display: flex; align-items: center; gap: 14px;
    color: var(--silver); font-weight: 500; font-size: 40px; letter-spacing: 1px;
  }
  .brand-square { width: 26px; height: 26px; background: currentColor; }
  .card--front { left: 570px; top: 550px; background: var(--card-white); overflow: hidden; }
  .front-pattern {
    position: absolute; inset: 0;
    background: linear-gradient(135deg, var(--pattern-light) 0%, var(--pattern-mid) 55%, var(--pattern-light) 100%);
  }
  .front-brand {
    position: absolute; left: 150px; top: 70px;
    color: var(--ink);
  }
  .front-brand__name {
    display: flex; align-items: center; gap: 9px;
    font-weight: 500; font-size: 30px; letter-spacing: .5px;
  }
  .front-brand__name .brand-square { width: 18px; height: 18px; }
  .front-brand__tagline {
    margin-left: 27px; margin-top: 2px;
    font-weight: 400; font-size: 12px; letter-spacing: 3.4px; text-transform: uppercase;
  }
  .person { position: absolute; left: 48px; top: 200px; }
  .person__name { font-weight: 300; font-size: 20px; color: var(--ink); }
  .person__role { font-weight: 300; font-style: italic; font-size: 15px; color: var(--accent); margin-top: 2px; }
  .contact {
    position: absolute; left: 300px; top: 150px;
    list-style: none; font-weight: 300; font-size: 11.5px; line-height: 1.45; color: var(--ink);
  }
  .contact__label { color: var(--accent); display: inline-block; width: 13px; }
  .contact__indent { padding-left: 13px; }
</style>
</head>
<body>
<main class="canvas">
  <section class="card card--back" aria-label="Kartenrückseite">
    <div class="back-brand"><span class="brand-square"></span>Velqora AG</div>
  </section>

  <section class="card card--front" aria-label="Kartenvorderseite">
    <div class="front-pattern" role="img" aria-label="Dezentes graues Polygonmuster als Hintergrund"></div>
    <div class="front-brand">
      <div class="front-brand__name"><span class="brand-square"></span>Velqora AG</div>
      <div class="front-brand__tagline">Digitale Strategien</div>
    </div>
    <div class="person">
      <p class="person__name">Mara Keller</p>
      <p class="person__role">Managing Director</p>
    </div>
    <ul class="contact">
      <li><span class="contact__label">A:</span>Lindenweg 12 60311.</li>
      <li class="contact__indent">Nordstadt.</li>
      <li><span class="contact__label">T:</span>+19 (0) 555 2187460</li>
      <li><span class="contact__label">F:</span>+19 (0) 555 2187461</li>
      <li><span class="contact__label">E:</span>hello@velqora.de</li>
      <li><span class="contact__label">W:</span>www.velqora.de</li>
    </ul>
  </section>
</main>
</body>
</html>
```